Virtualization software: PowerPoint, business cards

We're a young, small, dynamic application virtualization company: www.velrinta.com
We need a PowerPoint template + business cards. PDF background will be a plus.
This is mostly for enterprise clients.
Clean, professional, and most of all - following our website's colors.

Reason: Busy weekend; we'll need some more time to provide feedback & choose.

Target Market(s)

Corporate clients & investors.

Industry/Entity Type

Business

Requirements
Must have
• Clean, professional, and following our website's look: www.velrinta.com

```html
<!DOCTYPE html>
<html lang="en">
<head>
<meta charset="utf-8">
<title>Velrinta – Business Cards</title>
<link href="https://fonts.googleapis.com/css2?family=Open+Sans:wght@400;600;700&display=swap" rel="stylesheet">
<style>
  :root {
    --backdrop: #5b5d5f;
    --card-light: #f7f7f7;
    --card-light-edge: #e6e6e6;
    --card-dark: #111111;
    --card-dark-top: #1e1e1e;
    --ink: #222222;
    --ink-soft: #444444;
    --accent: #1e73be;
    --divider: #c4c4c4;
    --tagline: #8a8a8a;
    --white: #ffffff;
  }
  * { margin: 0; padding: 0; box-sizing: border-box; }
  html, body { width: 1200px; height: 849px; overflow: hidden; }
  body {
    background: var(--backdrop);
    font-family: "Open Sans", Arial, sans-serif;
    position: relative;
  }
  .card {
    position: absolute;
    left: 198px;
    width: 700px;
    height: 400px;
    border-radius: 22px;
    overflow: hidden;
    box-shadow: 0 4px 10px rgba(0,0,0,0.35);
  }
  .card--front {
    top: 18px;
    background: linear-gradient(180deg, var(--white) 0%, var(--card-light) 60%, var(--card-light-edge) 100%);
  }
  .card--back {
    top: 435px;
    background: linear-gradient(180deg, var(--card-dark-top) 0%, var(--card-dark) 55%, #050505 100%);
  }
  .wordmark {
    position: absolute;
    font-weight: 400;
    line-height: 1;
    white-space: nowrap;
  }
  .card--front .wordmark {
    left: 80px;
    top: 164px;
    font-size: 45px;
    letter-spacing: 11px;
    color: var(--ink);
  }
  .divider {
    position: absolute;
    left: 401px;
    top: 112px;
    width: 1px;
    height: 176px;
    background: var(--divider);
  }
  .contact {
    position: absolute;
    left: 436px;
    top: 111px;
  }
  .contact__name {
    font-size: 23px;
    font-weight: 600;
    color: var(--accent);
    line-height: 1.2;
  }
  .contact__role {
    font-size: 18px;
    color: var(--ink-soft);
    margin-top: 2px;
  }
  .contact__list {
    list-style: none;
    margin-top: 26px;
  }
  .contact__item {
    display: flex;
    align-items: center;
    height: 25px;
    font-size: 16.5px;
    color: var(--ink-soft);
  }
  .contact__item:first-child { font-size: 18px; }
  .contact__icon {
    width: 20px;
    height: 20px;
    margin-right: 16px;
    flex: none;
  }
  .gloss {
    position: absolute;
    left: 0; top: 0;
    width: 700px; height: 400px;
  }
  .card--back .wordmark {
    left: 0; right: 0;
    text-align: center;
    top: 137px;
    font-size: 77px;
    letter-spacing: 21px;
    padding-left: 21px;
    color: var(--white);
  }
  .tagline {
    position: absolute;
    left: 0; right: 0;
    top: 229px;
    text-align: center;
    font-size: 21px;
    color: var(--tagline);
  }
</style>
</head>
<body>

<section class="card card--front" aria-label="Business card front">
  <div class="wordmark">VELRINTA</div>
  <div class="divider"></div>
  <div class="contact">
    <div class="contact__name">John Doe</div>
    <div class="contact__role">Director</div>
    <ul class="contact__list">
      <li class="contact__item">
        <svg class="contact__icon" viewBox="0 0 20 20" aria-hidden="true">
          <defs><linearGradient id="iconFill" x1="0" y1="0" x2="0" y2="1"><stop offset="0" stop-color="#3a95de"/><stop offset="1" stop-color="#1565b0"/></linearGradient></defs>
          <rect width="20" height="20" rx="3" fill="url(#iconFill)"/>
          <path d="M6 4.5c-1 .6-1.6 1.6-1 3.2 1.2 3.2 4 6 7.2 7.3 1.5.6 2.6 0 3.2-1l-2.2-2-1.4 1c-1.6-.8-3-2.2-3.8-3.8l1-1.4z" fill="#fff"/>
        </svg>
        1234 5678 910
      </li>
      <li class="contact__item">
        <svg class="contact__icon" viewBox="0 0 20 20" aria-hidden="true">
          <rect width="20" height="20" rx="3" fill="url(#iconFill)"/>
          <rect x="4" y="6" width="12" height="8.5" fill="none" stroke="#fff" stroke-width="1.4"/>
          <path d="M4 6l6 5 6-5" fill="none" stroke="#fff" stroke-width="1.4"/>
        </svg>
        jdoe@velrinta.com
      </li>
      <li class="contact__item">
        <svg class="contact__icon" viewBox="0 0 20 20" aria-hidden="true">
          <rect width="20" height="20" rx="3" fill="url(#iconFill)"/>
          <g fill="none" stroke="#fff" stroke-width="1.2">
            <circle cx="10" cy="10" r="5.5"/>
            <ellipse cx="10" cy="10" rx="2.4" ry="5.5"/>
            <path d="M4.5 10h11M5.3 7.3h9.4M5.3 12.7h9.4"/>
          </g>
        </svg>
        www.velrinta.com
      </li>
    </ul>
  </div>
</section>

<section class="card card--back" aria-label="Business card back">
  <svg class="gloss" viewBox="0 0 700 400" aria-hidden="true">
    <defs>
      <linearGradient id="glossFill" x1="0" y1="0" x2="0" y2="1">
        <stop offset="0" stop-color="#ffffff" stop-opacity="0.08"/>
        <stop offset="1" stop-color="#ffffff" stop-opacity="0.03"/>
      </linearGradient>
    </defs>
    <path d="M0 0H700V228C560 188 380 178 0 206Z" fill="url(#glossFill)"/>
  </svg>
  <div class="wordmark">VELRINTA</div>
  <p class="tagline">Because every app should simply run, not install</p>
</section>

</body>
</html>
```